Business Card Design

we are a wellness center offering therapeutic massage modalities and yoga and meditation classes. I would like to see designs that incorporate the colors of my current logo (image uploaded) BUT I would like to change my logo slightly so that the three words wrapping around my image are: Calm Harbor Studio (in other words, take out skin).

Industry/Entity Type

Massage

Contact Information for Business Card

Lena R. Vasquez, MA, LMT, RYT-500, Founder
427 E. Dalton Ave., Suite 3C
Hampton, VA 23681
757-302-5947 (office)
757-541-2086 (cell)
calmharborstudio.net
calmharborstudio@mailbox-example.net

Requirements
Nice to have
• I'd like to have my logo as a watermark on the back side, but if that's not doable, no big deal. Thanks.

```html
<!DOCTYPE html>
<html lang="en">
<head>
<meta charset="utf-8">
<title>Calm Harbor Studio – Business Card</title>
<link href="https://fonts.googleapis.com/css2?family=Cinzel:wght@400&family=Tenor+Sans&display=swap" rel="stylesheet">
<style>
  :root {
    --backdrop: #e7e3dd;
    --card-cream: #f1eee7;
    --card-orange: #d6683c;
    --brand-orange: #d0643a;
    --mark-blue: #86b9c4;
    --mark-blue-light: #a9d6dc;
    --ink-brown: #4b3a31;
    --cream-text: #f6ede3;
  }
  * { margin: 0; padding: 0; box-sizing: border-box; }
  html, body {
    width: 1200px;
    height: 730px;
    overflow: hidden;
    background: var(--backdrop);
  }
  .canvas {
    width: 1200px;
    height: 730px;
    display: flex;
    align-items: center;
    justify-content: center;
    gap: 40px;
  }
  .card {
    position: relative;
    width: 520px;
    height: 297px;
    border-radius: 3px;
    box-shadow: 0 6px 18px rgba(60, 40, 30, 0.18);
    overflow: hidden;
  }

  /* Front */
  .card--front { background: var(--card-cream); }
  .front__brand {
    position: absolute;
    left: 36px;
    top: 30px;
    display: flex;
    align-items: center;
    gap: 18px;
  }
  .front__dot {
    width: 110px;
    height: 110px;
    border-radius: 50%;
    background: var(--mark-blue);
    flex-shrink: 0;
  }
  .brand-name {
    font-family: "Cinzel", serif;
    font-weight: 400;
    color: var(--brand-orange);
    font-size: 25px;
    letter-spacing: 1.5px;
    line-height: 1.1;
  }
  .front__name {
    position: absolute;
    left: 0;
    right: 0;
    top: 160px;
    text-align: center;
    font-family: "Cinzel", serif;
    font-weight: 400;
    font-size: 24px;
    color: var(--ink-brown);
    letter-spacing: 1px;
  }
  .front__contact {
    position: absolute;
    left: 16px;
    right: 16px;
    top: 212px;
    text-align: center;
    font-family: "Tenor Sans", sans-serif;
    font-size: 11.5px;
    line-height: 1.6;
    color: var(--ink-brown);
  }
  .front__contact .link { color: var(--brand-orange); }

  /* Back */
  .card--back {
    background: var(--card-orange);
    display: flex;
    align-items: center;
    padding-left: 44px;
    gap: 24px;
  }
  .back__dot {
    width: 150px;
    height: 150px;
    border-radius: 50%;
    background: var(--mark-blue-light);
    flex-shrink: 0;
  }
  .card--back .brand-name {
    color: var(--cream-text);
    font-size: 32px;
  }
</style>
</head>
<body>
  <main class="canvas">
    <section class="card card--front" aria-label="Business card front">
      <div class="front__brand">
        <div class="front__dot"></div>
        <div class="brand-name">Calm Harbor<br>Studio</div>
      </div>
      <h1 class="front__name">Lena R. Vasquez</h1>
      <p class="front__contact">
        MA, LMT, RYT-500, Founder 427 E. Dalton Ave., Suite 3C Linden Falls, OR 97411<br>
        P. 541-302-5947; C. 541-541-2086; E. <span class="link">calmharborstudio@mailbox-example.net</span><br>
        W. <span class="link">calmharborstudio.net</span>
      </p>
    </section>

    <section class="card card--back" aria-label="Business card back">
      <div class="back__dot"></div>
      <div class="brand-name">Calm Harbor<br>Studio</div>
    </section>
  </main>
</body>
</html>
```